Rehearsal studio business card design needed

My rehearsal studio i bought not that long ago was opened as a hobby originally and was definitely not taken seriously. I am trying to make the new look studio be launched with the new look business cards. I am looking for very simple and clean look cards to match the simple and clean studios. the colour scheme is red and grey. over all i am really just looking for a very simple card that is not too busy and just gets the point accross.
Target Market(s)
Targeting bands, music teachers, students, etc.
Industry/Entity Type
Business
Contact Information for Business Card
Bayridge Sound Centre
Rehearsal and Recording Facilities
Owen Barlow CEO
unit 8, 47 Garvin Road Tallow NSW 2093
0491 382 905
bayridgesoundcentre@mailvex.com
Requirements
Must have
- simplicity
Nice to have

```html
<!DOCTYPE html>
<html lang="en">
<head>
<meta charset="utf-8">
<title>Bayridge Sound Centre – Business Card</title>
<link href="https://fonts.googleapis.com/css2?family=Comfortaa:wght@400;700&display=swap" rel="stylesheet">
<style>
  :root {
    --page-bg: #e4e4e2;
    --card-black: #111111;
    --card-black-edge: #2a2a2a;
    --card-white: #f7f7f7;
    --brand-red: #d8202c;
    --brand-grey: #9a9ea1;
    --text-light: #f2f2f2;
    --text-dark: #1a1a1a;
  }
  * { box-sizing: border-box; margin: 0; padding: 0; }
  html, body {
    width: 1200px; height: 1000px; overflow: hidden;
    background: var(--page-bg);
    font-family: "Comfortaa", sans-serif;
  }
  .sheet {
    position: relative; width: 1200px; height: 1000px;
  }
  .card {
    position: absolute; left: 250px; width: 700px; height: 400px;
    border-radius: 4px;
    box-shadow: 0 8px 24px rgba(0,0,0,0.18);
    overflow: hidden;
  }
  /* Front */
  .card--front {
    top: 70px;
    background: linear-gradient(135deg, var(--card-black-edge) 0%, var(--card-black) 55%);
    color: var(--text-light);
  }
  .front__tagline {
    position: absolute; top: 30px; left: 40px;
    font-size: 15px; letter-spacing: 0.2px;
  }
  .front__brand {
    position: absolute; top: 78px; left: 40px;
    display: flex; align-items: center; gap: 14px;
  }
  .brand-dot {
    width: 26px; height: 26px; border-radius: 50%;
    background: var(--brand-red);
  }
  .brand-name {
    font-size: 22px; font-weight: 700; color: var(--text-light);
  }
  .front__person {
    position: absolute; top: 70px; right: 46px; text-align: right;
  }
  .person__name { font-size: 38px; font-weight: 700; }
  .person__role { font-size: 14px; font-weight: 700; margin-top: 6px; }
  .front__contacts {
    position: absolute; left: 40px; bottom: 40px;
    list-style: none;
  }
  .contact {
    display: flex; align-items: center; gap: 16px;
    font-size: 17px; margin-top: 16px;
  }
  .contact svg { width: 24px; height: 24px; flex: none; }
  .contact-group__label {
    font-size: 30px; font-weight: 700; margin-bottom: 4px;
  }
  /* Back */
  .card--back {
    top: 530px;
    background: radial-gradient(circle at 40% 40%, #ffffff 0%, var(--card-white) 55%, #dedede 100%);
    color: var(--text-dark);
    display: flex; align-items: center; justify-content: center; gap: 22px;
  }
  .back__dot {
    width: 70px; height: 70px; border-radius: 50%;
    background: var(--brand-red);
  }
  .back__name {
    font-size: 44px; font-weight: 700; color: var(--text-dark);
  }
</style>
</head>
<body>
<main class="sheet">
  <section class="card card--front" aria-label="Business card front">
    <p class="front__tagline">Bayridge Sound Centre Rehearsal and Recording Facilities</p>
    <div class="front__brand">
      <span class="brand-dot"></span>
      <span class="brand-name">Bayridge Sound Centre</span>
    </div>
    <div class="front__person">
      <p class="person__name">Owen Barlow</p>
      <p class="person__role">CEO</p>
    </div>
    <ul class="front__contacts">
      <li class="contact-group__label">bayridge</li>
      <li class="contact">
        <svg viewBox="0 0 24 24" aria-hidden="true"><rect x="7" y="3" width="10" height="18" rx="2" fill="none" stroke="#d8202c" stroke-width="2"/><circle cx="12" cy="17.5" r="1.2" fill="#d8202c"/></svg>
        <span>2093 0491 382 905</span>
      </li>
      <li class="contact">
        <svg viewBox="0 0 24 24" aria-hidden="true"><circle cx="12" cy="12" r="10" fill="none" stroke="#d8202c" stroke-width="2"/><rect x="7" y="8.5" width="10" height="7" fill="none" stroke="#d8202c" stroke-width="1.6"/><path d="M7 8.5l5 4 5-4" fill="none" stroke="#d8202c" stroke-width="1.6"/></svg>
        <span>bayridgesoundcentre@mailvex.com</span>
      </li>
      <li class="contact">
        <svg viewBox="0 0 24 24" aria-hidden="true"><path d="M12 22s-7-7.5-7-12.5a7 7 0 0 1 14 0C19 14.5 12 22 12 22z" fill="none" stroke="#d8202c" stroke-width="2"/><circle cx="12" cy="9.5" r="2.5" fill="#d8202c"/></svg>
        <span>unit 8, 47 Garvin Road Tallow NSW</span>
      </li>
    </ul>
  </section>

  <section class="card card--back" aria-label="Business card back">
    <span class="back__dot"></span>
    <span class="back__name">Bayridge Sound Centre</span>
  </section>
</main>
</body>
</html>
```